Welcome Series Email: 1st Email in Series BargainLifts.net

I am working to create a three part welcome series email for visitors to my website but I need a little help getting a creative look and feel that looks professional. I am just looking for some help with the design of the 1st email that we can then develop the first email with and pass down some of the creative elements to the next two emails in the series. My site is BargainLifts.net and we sell a broad range of products from motorcycle all the way to wheelchair and mobility so I need to be mindful of all the different customer types. I have a prototype of the 1st email that my email service provider created that is attached and I just am not happy with the design. I would be interested if someone could take the general concept of this email and give it better look. If you have a completely different idea I am open to that as well. The design I choose does not have to be the perfect final product just a great shell that will dictate the look and feel of all emails I send to my customer list.
Thanks for your help!

Industry/Entity Type

Product

```html
<!DOCTYPE html>
<html lang="en">
<head>
<meta charset="utf-8">
<title>Welcome to Bargain Lifts</title>
<link rel="stylesheet" href="https://fonts.googleapis.com/css2?family=Arvo:wght@700&family=Open+Sans:wght@300;400;600;700;800&display=swap">
<style>
  :root {
    --red: #c8161d;
    --red-dark: #8e0f14;
    --navy: #1b2a63;
    --navy-deep: #0f1a48;
    --navy-light: #2c3f8a;
    --page: #efefef;
    --ink: #1e1e1e;
    --muted: #3a3a3a;
    --white: #ffffff;
  }
  * { box-sizing: border-box; margin: 0; padding: 0; }
  html, body { width: 1200px; height: 2416px; overflow: hidden; }
  body {
    position: relative;
    background: var(--page);
    font-family: "Open Sans", Arial, sans-serif;
    color: var(--ink);
  }

  /* Hero */
  .hero {
    position: absolute; left: 0; top: 0; width: 1200px; height: 855px;
    background: linear-gradient(180deg, #dfe7ee 0%, #c9d3dc 35%, #eef2f5 70%, #f3f3f3 100%);
  }
  .hero-ride {
    position: absolute; left: 490px; top: 330px; width: 670px; height: 500px;
    background: radial-gradient(ellipse at 50% 55%, #2b2f3a 0%, #4a5262 45%, rgba(200,210,220,0) 72%);
  }
  .brand {
    position: absolute; left: 150px; top: 70px;
    display: flex; align-items: center; gap: 14px;
    font-family: "Open Sans", Arial, sans-serif; font-weight: 800;
    font-size: 40px; color: var(--navy);
  }
  .brand-mark { width: 26px; height: 26px; background: var(--red); border-radius: 50%; }
  .welcome {
    position: absolute; left: 74px; top: 267px; width: 421px; height: 563px;
    background: linear-gradient(180deg, var(--navy-light) 0%, var(--navy) 45%, var(--navy-deep) 100%);
    text-align: center; color: var(--white);
  }
  .welcome-title {
    margin-top: 64px;
    font-family: "Arvo", Georgia, serif; font-size: 45px; line-height: 1;
  }
  .welcome-name {
    margin-top: 6px;
    font-family: "Arvo", Georgia, serif; font-size: 31px; color: var(--red);
    text-transform: uppercase;
  }
  .welcome-copy {
    margin: 26px 28px 0; font-weight: 300; font-size: 37px; line-height: 50px;
  }
  .cta {
    position: absolute; left: 122px; top: 768px; width: 326px; height: 90px;
    background: var(--red); color: var(--white);
    font-weight: 700; font-size: 23px; letter-spacing: .3px;
    display: flex; align-items: center; justify-content: center;
    box-shadow: 0 3px 6px rgba(0,0,0,.25);
  }
  .cta-fold { position: absolute; left: 100px; top: 830px; width: 22px; height: 28px; background: var(--red-dark); }
  .slider-tab {
    position: absolute; right: 0; top: 519px; width: 61px; height: 125px;
    background: var(--red); border-radius: 10px 0 0 10px;
    display: flex; flex-direction: column; align-items: center; justify-content: center; gap: 10px;
  }
  .slider-dot { width: 12px; height: 12px; border-radius: 50%; background: var(--red-dark); }
  .slider-dot.is-active { background: var(--white); }

  /* Call strip */
  .call { position: absolute; left: 0; top: 940px; width: 1200px; text-align: center; }
  .call-label { font-weight: 800; font-size: 31px; color: var(--navy); line-height: 1; }
  .call-number { font-weight: 800; font-size: 70px; color: var(--red); line-height: 1.05; letter-spacing: -1px; }
  .call-rule { position: absolute; top: 52px; height: 2px; background: var(--red); opacity: .6; }
  .call-rule.left { left: 74px; width: 280px; }
  .call-rule.right { left: 846px; width: 282px; }

  /* Collections */
  .collection { position: absolute; width: 243px; text-align: center; }
  .collection-photo { width: 243px; height: 183px; box-shadow: 0 8px 14px rgba(0,0,0,.22); }
  .collection-name {
    margin-top: 24px; font-weight: 700; font-size: 22px; line-height: 28px;
    text-transform: uppercase; color: var(--ink);
  }

  /* Perks band */
  .perks { position: absolute; left: 0; top: 1640px; width: 1200px; height: 435px; }
  .perks svg { position: absolute; left: 0; top: 0; }
  .perks-lead {
    position: absolute; left: 0; top: 60px; width: 1200px; text-align: center;
    color: var(--white); font-weight: 700; font-size: 28px; line-height: 38px;
  }
  .perks-sub {
    position: absolute; left: 0; top: 138px; width: 1200px; text-align: center;
    color: var(--white); font-size: 22px;
  }
  .perk {
    position: absolute; top: 192px; width: 335px; height: 175px;
    background: radial-gradient(ellipse at 50% 30%, var(--navy-light) 0%, var(--navy) 55%, var(--navy-deep) 100%);
    border: 3px solid #3b4fa0; border-radius: 12px;
    color: var(--white); text-align: center;
    display: flex; flex-direction: column; align-items: center; justify-content: center; gap: 18px;
    font-weight: 700; font-size: 22px; line-height: 28px; text-transform: uppercase;
  }

  /* Footer */
  .footer { position: absolute; left: 0; top: 2100px; width: 1200px; text-align: center; }
  .follow { font-weight: 700; font-size: 29px; }
  .social { display: flex; justify-content: center; gap: 24px; margin-top: 18px; }
  .social-item { width: 42px; height: 42px; background: var(--red); border-radius: 6px; }
  .legal { margin-top: 20px; font-size: 13px; line-height: 27px; color: var(--muted); }
  .notice { margin: 28px auto 0; width: 1000px; font-size: 17px; line-height: 27px; color: var(--navy); }
  .links { margin-top: 13px; font-size: 17px; color: var(--ink); }
  .code { position: absolute; right: 26px; top: 2368px; font-size: 13px; color: var(--muted); }
</style>
</head>
<body>

<section class="hero">
  <div class="hero-ride" role="img" aria-label="Two riders on a snowmobile in a snowy pine forest"></div>
  <div class="brand"><span class="brand-mark"></span>BargainLifts.net</div>
  <div class="welcome">
    <h1 class="welcome-title">WELCOME TO</h1>
    <div class="welcome-name">Bargain Lifts</div>
    <p class="welcome-copy">See how we are bringing people to new heights with ramps for just about any occasion</p>
  </div>
  <div class="cta-fold"></div>
  <div class="cta">VIEW ALL COLLECTIONS</div>
  <div class="slider-tab">
    <span class="slider-dot is-active"></span><span class="slider-dot"></span><span class="slider-dot"></span>
  </div>
</section>

<section class="call">
  <span class="call-rule left"></span><span class="call-rule right"></span>
  <div class="call-label">CALL OUR PRODUCT EXPERTS</div>
  <div class="call-number">888-555-0142</div>
</section>

<section class="collections">
  <div class="collection" style="left:74px;top:1095px">
    <div class="collection-photo" role="img" aria-label="Snowmobile rider kicking up snow" style="background:linear-gradient(160deg,#b9c6cf,#eef1f3 60%,#c9a66a)"></div>
    <div class="collection-name">Powersports</div>
  </div>
  <div class="collection" style="left:343px;top:1095px">
    <div class="collection-photo" role="img" aria-label="Power wheelchair on white background" style="background:radial-gradient(circle at 50% 50%,#2a2a2a 0%,#555 25%,#fafafa 48%)"></div>
    <div class="collection-name">Wheelchair &amp;<br>Mobility</div>
  </div>
  <div class="collection" style="left:614px;top:1095px">
    <div class="collection-photo" role="img" aria-label="Forklift moving a cardboard box in a warehouse" style="background:linear-gradient(90deg,#d9dbdc,#c85a3a 45%,#c7a57a 80%,#e2e2e2)"></div>
    <div class="collection-name">Commercial &amp;<br>Utility</div>
  </div>
  <div class="collection" style="left:884px;top:1095px">
    <div class="collection-photo" role="img" aria-label="Silver car speeding on a road" style="background:linear-gradient(135deg,#5d7f9a,#c9c9c9 45%,#c58b4c)"></div>
    <div class="collection-name">Automotive</div>
  </div>
  <div class="collection" style="left:74px;top:1373px">
    <div class="collection-photo" role="img" aria-label="Cyclist riding at sunset" style="background:linear-gradient(180deg,#3a3f55,#d07a3a 55%,#3b3f2f)"></div>
    <div class="collection-name">Recreation</div>
  </div>
  <div class="collection" style="left:343px;top:1373px">
    <div class="collection-photo" role="img" aria-label="Woman hugging a golden retriever outdoors" style="background:linear-gradient(120deg,#6b8f3a,#e3c08f 50%,#c07a30)"></div>
    <div class="collection-name">Pet</div>
  </div>
  <div class="collection" style="left:614px;top:1373px">
    <div class="collection-photo" role="img" aria-label="Front yard garden with a wheelbarrow" style="background:linear-gradient(180deg,#cfcab8,#8a6a4a 45%,#4f8a2e)"></div>
    <div class="collection-name">Home &amp; Garden</div>
  </div>
  <div class="collection" style="left:884px;top:1373px">
    <div class="collection-photo" role="img" aria-label="Custom threshold ramp at a doorway" style="background:linear-gradient(180deg,#3a3a3a,#8a8a8a 50%,#c9b27a)"></div>
    <div class="collection-name">Custom Ramps</div>
  </div>
</section>

<section class="perks">
  <svg width="1200" height="435" viewBox="0 0 1200 435" aria-hidden="true">
    <path d="M0 30 Q600 -20 1200 30 L1200 405 Q600 455 0 405 Z" fill="#c8161d"/>
  </svg>
  <p class="perks-lead">As a member of our special e-mail program you will be the first to hear<br>about new products,exclusive offers and upcoming sales events.</p>
  <p class="perks-sub">Our low prices,fast shipping and 100% money back gurantee truly set us apart in the industry</p>

  <div class="perk" style="left:74px">
    <svg width="60" height="60" viewBox="0 0 60 60" aria-hidden="true">
      <path d="M8 30 L30 8 L52 8 L52 30 L30 52 Z" fill="#fff" transform="rotate(-10 30 30)"/>
      <circle cx="44" cy="15" r="4" fill="#1b2a63"/>
      <text x="31" y="37" font-family="Open Sans, sans-serif" font-weight="700" font-size="16" fill="#1b2a63" text-anchor="middle">%</text>
    </svg>
    <span>Discount Prices</span>
  </div>
  <div class="perk" style="left:432px">
    <svg width="66" height="50" viewBox="0 0 66 50" aria-hidden="true">
      <rect x="2" y="6" width="38" height="28" rx="2" fill="#fff"/>
      <path d="M42 14 H54 L63 25 V34 H42 Z" fill="#fff"/>
      <circle cx="14" cy="40" r="7" fill="#fff" stroke="#1b2a63" stroke-width="3"/>
      <circle cx="52" cy="40" r="7" fill="#fff" stroke="#1b2a63" stroke-width="3"/>
    </svg>
    <span>Fast Shipping</span>
  </div>
  <div class="perk" style="left:794px">
    <svg width="72" height="48" viewBox="0 0 72 48" aria-hidden="true">
      <rect x="2" y="2" width="68" height="44" rx="3" fill="#fff"/>
      <rect x="8" y="8" width="56" height="32" fill="none" stroke="#1b2a63" stroke-width="2"/>
      <circle cx="36" cy="24" r="11" fill="#1b2a63"/>
      <text x="36" y="30" font-family="Open Sans, sans-serif" font-weight="700" font-size="15" fill="#fff" text-anchor="middle">1</text>
    </svg>
    <span>100% Money Back<br>Guarantee.</span>
  </div>
</section>

<footer class="footer">
  <div class="follow">Follow Us !</div>
  <div class="social" aria-label="Social channels">
    <span class="social-item"></span><span class="social-item"></span><span class="social-item"></span>
    <span class="social-item"></span><span class="social-item"></span><span class="social-item"></span>
  </div>
  <p class="legal">© Copyright 2000-2014 Bargain Lifts All Rights Reserved<br>418 N Harbor St &nbsp;| &nbsp;Lakeview WI 53000</p>
  <p class="notice">This e-mail was sent to #mailhub\e-mail# by hello@bargainlifts.net you are receiving this advertisement at your request.This is a recurring mailing we respect your privacy</p>
  <p class="links">Please review our privacy policy &nbsp;| &nbsp;Unsubscribe from receiving future communication</p>
</footer>
<span class="code">C5</span>

</body>
</html>
```